Mapping of agricultural parcels

Creation in January 2019 of the LORIVEX company, specialized in capturing, exploiting and distributing aerial images for agriculture. Need to communicate on a brochure to make known the existence of the company and the services and services offered to agricultural laboratories, and farmers and agricultural cooperatives. The brochure should highlight the return on investment (ROI) and the relevance of services for the development of sustainable agriculture. To carry out its missions, the company has expertise in: - piloting drones (operator and remote pilot) - building and distributing maps - in web & mobile development

Target Market(s)

Exploitation and agricultural cooperative Laboratory of Agronomy Industrial in the agri-food sector

Font styles to use
Serif

Colors
00a990
ffffff
5c5c5c

Requirements
Must have
• to present the proposed services to present the advantages for the client to present the mode of operation and the contacts (see website www.parcelvue-example.fr)
Nice to have
• - Sustainable agriculture - Biomass map and Modulation - Return on investment - Clear and simple aspect - Functional and practical aspect put forward
Should not have
• - too much color - complicated (too much to read) - too elegant

```html
<!DOCTYPE html>
<html lang="fr">
<head>
<meta charset="utf-8">
<title>LORIVEX – Brochure</title>
<link href="https://fonts.googleapis.com/css2?family=Arimo:wght@400;700&family=PT+Sans:wght@400;700&family=PT+Sans+Narrow:wght@400;700&family=Nunito:wght@800&display=swap" rel="stylesheet">
<style>
  :root{
    --slate:#3c4e5b;
    --slate-deep:#324350;
    --green:#4b9b31;
    --green-soft:#6cb84c;
    --white:#ffffff;
    --ink:#3a4650;
    --stage:#e7e7e5;
    --sky-top:#9fc7df;
    --sky-low:#e6f0f5;
    --field:#5d8a3a;
    --field-dark:#3f6a2a;
    --crop:#d9a83e;
  }
  *{margin:0;padding:0;box-sizing:border-box}
  html,body{width:1200px;height:816px;overflow:hidden;background:var(--stage)}
  body{position:relative;font-family:"PT Sans",Arial,sans-serif;color:var(--ink)}
  .page{position:absolute;top:12px;width:560px;height:792px;background:var(--white);overflow:hidden;box-shadow:0 2px 8px rgba(0,0,0,.15)}
  .page--front{left:30px}
  .page--back{left:610px}
  .layer{position:absolute;left:0;top:0;width:560px;height:792px}
  .brand{position:absolute;top:22px;display:flex;align-items:center;gap:12px}
  .brand__dot{width:20px;height:20px;border-radius:50%;background:var(--green)}
  .brand__name{font-family:"Nunito",Arial,sans-serif;font-weight:800;font-size:40px;color:var(--slate);letter-spacing:1px}
  .page--front .brand{left:48px}
  .page--back .brand{right:30px}
  .headline{position:absolute;left:17px;top:166px;font-family:"Arimo",Arial,sans-serif;font-size:23px;line-height:30px;color:var(--white);letter-spacing:.3px}
  .expertise{position:absolute;left:17px;top:388px;width:240px;font-family:"PT Sans Narrow",Arial,sans-serif;font-weight:700;font-size:14.5px;line-height:18px;color:var(--white)}
  .intro{position:absolute;left:20px;top:436px;width:222px;font-size:10.6px;line-height:13.3px;color:var(--white);text-align:justify}
  .intro p{margin-bottom:12px}
  .sectors{position:absolute;left:20px;top:663px;list-style:none;font-family:"PT Sans Narrow",Arial,sans-serif;font-size:11px;color:var(--white)}
  .sectors li{display:flex;align-items:center;gap:7px;height:17px}
  .sectors svg{width:11px;height:11px}
  .services-title{position:absolute;left:272px;top:405px;font-family:"PT Sans Narrow",Arial,sans-serif;font-weight:700;font-size:14.5px;color:var(--green)}
  .services{position:absolute;left:272px;top:433px;width:280px;list-style:none}
  .services li{display:flex;align-items:center;gap:8px;height:33px;font-size:10.4px;line-height:12px;color:var(--ink)}
  .services__icon{flex:none;width:25px;height:25px;border-radius:50%;background:var(--green);display:flex;align-items:center;justify-content:center}
  .services__icon svg{width:13px;height:13px}
  .thumb{position:absolute;border-radius:6px;border:2px solid var(--white);box-shadow:0 1px 4px rgba(0,0,0,.25)}
  .footer{position:absolute;left:0;bottom:0;width:560px;height:48px}
  .footer__band{position:absolute;left:0;top:0;width:560px;height:48px}
  .footer__phone{position:absolute;left:22px;top:13px;display:flex;align-items:center;gap:7px;font-family:"Arimo",Arial,sans-serif;font-size:16px;color:var(--white)}
  .footer__phone svg{width:16px;height:16px}
  .footer__web{position:absolute;left:222px;top:17px;font-family:"Arimo",Arial,sans-serif;font-size:10.5px;letter-spacing:.4px;color:var(--white);white-space:nowrap}
  .col{position:absolute;top:452px;font-size:8.4px;line-height:9.6px}
  .col--dark{left:20px;width:218px;color:var(--white)}
  .col--light{left:266px;width:280px;color:var(--ink)}
  .col h3{font-weight:400;font-size:9.6px;line-height:10.4px;margin-bottom:6px}
  .col--dark h3{color:var(--green-soft)}
  .col--light h3{color:var(--green)}
  .col ul{list-style:none;margin-bottom:10px}
  .col li{position:relative;padding-left:10px;margin-bottom:3px}
  .col li::before{content:"";position:absolute;left:1px;top:2.5px;width:5px;height:5px;border:1px solid var(--green-soft);border-radius:50%}
</style>
</head>
<body>

<!-- FRONT PAGE -->
<section class="page page--front">
  <svg class="layer" viewBox="0 0 560 792" role="img" aria-label="Photo: a quadcopter drone flying in a blue sky above a green crop field and a village">
    <defs>
      <linearGradient id="frontPhoto" x1="0" y1="0" x2="0" y2="1">
        <stop offset="0" stop-color="var(--sky-top)"/>
        <stop offset=".6" stop-color="var(--sky-low)"/>
        <stop offset=".72" stop-color="var(--field)"/>
        <stop offset="1" stop-color="var(--field-dark)"/>
      </linearGradient>
    </defs>
    <path d="M0,30 L560,0 V372 Q560,394 538,397 L262,432 L0,432 Z" fill="url(#frontPhoto)"/>
  </svg>
  <svg class="layer" viewBox="0 0 560 792" aria-hidden="true">
    <path d="M0,74 L312,60 L268,330 L0,330 Z" fill="var(--slate)" opacity=".93"/>
    <path d="M0,330 L268,330 L258,400 L0,400 Z" fill="var(--slate)" opacity=".72"/>
    <path d="M0,400 L258,400 L250,744 L0,744 Z" fill="var(--slate)"/>
    <path d="M0,0 H560 V8 L195,112 Q170,119 148,114 L0,86 Z" fill="var(--white)"/>
  </svg>

  <div class="brand"><span class="brand__dot"></span><span class="brand__name">LORIVEX</span></div>

  <h1 class="headline">GAGNER EN EFFICIENCE<br>EN PRENANT DE LA<br>HAUTEUR</h1>

  <h2 class="expertise">EXPERTISE EN CAPTATION ET<br>TRAITEMENT D'IMAGES AERIENNES</h2>
  <div class="intro">
    <p>Contribuer au développement d’une agriculture plus raisonnée en développant la surveillance de vos cultures avec l’imagerie aérienne par drones</p>
    <p>Cartographier précisément vos parcelles avec l’exploitation (technologie RTK) pour mesurer et délimiter précisément vos surfaces agricoles</p>
    <p>Maitriser vos apports d’intrants par la modulation déduite de l’observation de vos cultures dans les domaines multi-spectraux et réaliser des économies tout en préservant les ressources naturelles</p>
  </div>

  <ul class="sectors">
    <li><svg viewBox="0 0 12 12"><rect x=".5" y=".5" width="11" height="11" rx="2" fill="none" stroke="var(--green-soft)"/><path d="M3,6 L5.2,8.2 L9.5,3.5" fill="none" stroke="var(--green-soft)" stroke-width="1.4"/></svg>AGRICULTURE DE PRECISION</li>
    <li><svg viewBox="0 0 12 12"><rect x=".5" y=".5" width="11" height="11" rx="2" fill="none" stroke="var(--green-soft)"/><path d="M3,6 L5.2,8.2 L9.5,3.5" fill="none" stroke="var(--green-soft)" stroke-width="1.4"/></svg>SUIVI DE CHANTIER</li>
    <li><svg viewBox="0 0 12 12"><rect x=".5" y=".5" width="11" height="11" rx="2" fill="none" stroke="var(--green-soft)"/><path d="M3,6 L5.2,8.2 L9.5,3.5" fill="none" stroke="var(--green-soft)" stroke-width="1.4"/></svg>INSPECTION D'OUVRAGE</li>
    <li><svg viewBox="0 0 12 12"><rect x=".5" y=".5" width="11" height="11" rx="2" fill="none" stroke="var(--green-soft)"/><path d="M3,6 L5.2,8.2 L9.5,3.5" fill="none" stroke="var(--green-soft)" stroke-width="1.4"/></svg>MINES ET CARRIÈRES</li>
  </ul>

  <h2 class="services-title">NOS PRESTATIONS</h2>
  <ul class="services">
    <li><span class="services__icon"><svg viewBox="0 0 14 14"><circle cx="7" cy="7" r="4" fill="none" stroke="var(--white)" stroke-width="1.6"/></svg></span>Photographies aériennes de vos parcelles agricoles à différents stades de leur développement</li>
    <li><span class="services__icon"><svg viewBox="0 0 14 14"><rect x="2" y="3" width="10" height="8" fill="none" stroke="var(--white)" stroke-width="1.5"/></svg></span>Constitution de cartes pour la surveillance de vos cultures (mesure de la biomasse, carte de zonage,…)</li>
    <li><span class="services__icon"><svg viewBox="0 0 14 14"><circle cx="7" cy="7" r="4" fill="var(--white)"/></svg></span>Mise à disposition de carte de prescription (carte de zonage) pour la modulation manuelle ou automatique</li>
    <li><span class="services__icon"><svg viewBox="0 0 14 14"><rect x="2.5" y="4" width="9" height="6" rx="3" fill="var(--white)"/></svg></span>Vos cartes mis à disposition sur le cloud privé via une application dédiée</li>
    <li><span class="services__icon"><svg viewBox="0 0 14 14"><circle cx="4" cy="4" r="2" fill="none" stroke="var(--white)" stroke-width="1.3"/><circle cx="10" cy="4" r="2" fill="none" stroke="var(--white)" stroke-width="1.3"/><circle cx="4" cy="10" r="2" fill="none" stroke="var(--white)" stroke-width="1.3"/><circle cx="10" cy="10" r="2" fill="none" stroke="var(--white)" stroke-width="1.3"/></svg></span>Formation au pilotage de drones et à l’exploitation de l’imagerie aérienne en milieu agricole</li>
    <li><span class="services__icon"><svg viewBox="0 0 14 14"><path d="M7,13 C3,8.5 3,6.5 3,5.5 A4,4 0 0 1 11,5.5 C11,6.5 11,8.5 7,13 Z" fill="var(--white)"/><circle cx="7" cy="5.5" r="1.5" fill="var(--green)"/></svg></span>Relever précisément vos sinistres par la photographie aérienne</li>
  </ul>

  <div class="thumb" style="left:192px;top:642px;width:111px;height:94px;background:linear-gradient(135deg,#e0402a,#f07a2a 40%,#f2d23a 70%,#9cc64a)" role="img" aria-label="Colour biomass map of a parcel"></div>
  <div class="thumb" style="left:307px;top:642px;width:120px;height:94px;background:linear-gradient(135deg,#9a9a96,#5f605c 50%,#b9b8b2)" role="img" aria-label="Aerial view of a construction site"></div>
  <div class="thumb" style="left:431px;top:642px;width:120px;height:94px;background:linear-gradient(135deg,#c99464,#a8703f 50%,#d8b48c)" role="img" aria-label="Aerial view of a quarry"></div>

  <footer class="footer">
    <svg class="footer__band" viewBox="0 0 560 48" aria-hidden="true">
      <rect x="0" y="0" width="560" height="3" fill="var(--green)"/>
      <path d="M0,5 H560 V48 H0 Z" fill="var(--slate)"/>
      <path d="M0,5 H210 L198,48 H0 Z" fill="var(--green)"/>
      <path d="M213,5 H217 L205,48 H201 Z" fill="var(--white)"/>
    </svg>
    <div class="footer__phone"><svg viewBox="0 0 16 16"><circle cx="8" cy="8" r="7" fill="none" stroke="var(--white)" stroke-width="1.4"/><path d="M5.5,4.5 L6.8,4.3 L7.4,6.2 L6.6,6.9 Q7.4,8.7 9.1,9.4 L9.8,8.6 L11.7,9.2 L11.5,10.5 Q8.5,11.2 6.5,9.3 Q4.6,7.3 5.5,4.5 Z" fill="var(--white)"/></svg>(+33) 3.10.20.30.40</div>
    <div class="footer__web">www.parcelvue-example.fr &nbsp;|&nbsp; contact@parcelvue-example.fr</div>
  </footer>
</section>

<!-- BACK PAGE -->
<section class="page page--back">
  <svg class="layer" viewBox="0 0 560 792" role="img" aria-label="Photo: a green maize field next to a golden wheat field with a professional drone in flight">
    <defs>
      <linearGradient id="backPhoto" x1="0" y1="0" x2="1" y2="0">
        <stop offset="0" stop-color="var(--field-dark)"/>
        <stop offset=".45" stop-color="var(--field)"/>
        <stop offset=".6" stop-color="var(--crop)"/>
        <stop offset="1" stop-color="#e2bd66"/>
      </linearGradient>
    </defs>
    <path d="M0,30 L560,30 V330 Q560,352 538,355 L247,408 L0,408 Z" fill="url(#backPhoto)"/>
  </svg>
  <svg class="layer" viewBox="0 0 560 792" aria-hidden="true">
    <path d="M0,34 L286,30 L252,330 L0,330 Z" fill="var(--slate)" opacity=".72"/>
    <path d="M0,330 L252,330 L247,410 L0,410 Z" fill="var(--slate)" opacity=".82"/>
    <path d="M0,410 L247,410 L247,744 L0,744 Z" fill="var(--slate)"/>
    <path d="M0,0 H560 V124 Q560,140 544,142 Q420,116 0,34 Z" fill="var(--white)"/>
  </svg>

  <div class="brand"><span class="brand__dot"></span><span class="brand__name">LORIVEX</span></div>

  <h1 class="headline">GAGNER EN EFFICIENCE<br>EN PRENANT DE LA<br>HAUTEUR</h1>

  <div class="thumb" style="left:24px;top:348px;width:97px;height:84px;background:linear-gradient(180deg,#f0a24a,#c76a2a 55%,#5a3a22)" role="img" aria-label="Drone over a field at sunset"></div>
  <div class="thumb" style="left:127px;top:348px;width:95px;height:84px;background:linear-gradient(135deg,#a8a59c,#d8cf5a 45%,#8e8b84)" role="img" aria-label="Aerial view of a quarry with a marked zone"></div>
  <div class="thumb" style="left:228px;top:348px;width:95px;height:84px;background:linear-gradient(135deg,#4f86c6,#8fb5df 55%,#e8eef5)" role="img" aria-label="Wind turbine blade under inspection"></div>

  <div class="col col--dark">
    <h3>Photographies aériennes de vos parcelles agricoles à différents stades de leur développement:</h3>
    <ul>
      <li>Mieux observer pour optimiser et cibler vos actions</li>
      <li>Développer votre pro-activité en anticipant sur les besoins de vos plantes</li>
      <li>Optimiser votre temps et vos ressources</li>
      <li>Echanger avec votre conseillers agricoles sur la base d’une radiographie de vos parcelles</li>
    </ul>
    <h3>Constitution de cartes pour la surveillance de vos cultures (mesure de la biomasse, carte de zonage,…)</h3>
    <ul>
      <li>Anticiper sur la survenue de maladie</li>
      <li>Identifier les zones à problème</li>
    </ul>
    <h3>Mise à disposition de carte de prescription (carte de zonage) pour la modulation manuelle ou automatique</h3>
    <ul>
      <li>Cartes de zonage déduite des mesure de biomasse</li>
      <li>Moduler vos apports en fonction des zones identifiées</li>
      <li>Maitriser les intrants</li>
    </ul>
  </div>

  <div class="col col--light">
    <h3>Vos cartes mis à disposition sur le cloud privé via une application dédiée</h3>
    <ul>
      <li>Vos parcelles implantées sur le teritoires</li>
      <li>Toutes vos cartes dans un même logiciel consultable depuis votre ordinateur ou votre smartphone</li>
      <li>Cartes compatibles et intégrables dans le logiciel « parcelle »</li>
      <li>Comparer et partager facilement vos données entre exploitations</li>
    </ul>
    <h3>Formation au pilotage de drones et à l’exploitation de l’imagerie aérienne en milieu agricole</h3>
    <ul>
      <li>Apport de l’imagerie aérienne en milieu agricole</li>
      <li>Usage du drone en milieu agricole</li>
      <li>Réglementation et pilotage du drones</li>
      <li>Intégration des cartes dans vos logiciels</li>
      <li>Comment interpréter les cartes (ortho-photos, cartes NDVI, NDRE, …)</li>
      <li>La modulation Manuelle et Automatique</li>
    </ul>
    <h3>Relever précisément vos sinistres par la photographie aérienne</h3>
    <ul>
      <li>Identifier et mesurer le périmètre</li>
      <li>Délimiter précisément les zones concernées</li>
      <li>Evaluer précisément votre indemnisation en fournissant les éléments factuels à votre assureur</li>
    </ul>
  </div>

  <footer class="footer">
    <svg class="footer__band" viewBox="0 0 560 48" aria-hidden="true">
      <rect x="0" y="0" width="560" height="3" fill="var(--green)"/>
      <path d="M0,5 H560 V48 H0 Z" fill="var(--slate)"/>
      <path d="M0,5 H210 L198,48 H0 Z" fill="var(--green)"/>
      <path d="M213,5 H217 L205,48 H201 Z" fill="var(--white)"/>
    </svg>
    <div class="footer__phone"><svg viewBox="0 0 16 16"><circle cx="8" cy="8" r="7" fill="none" stroke="var(--white)" stroke-width="1.4"/><path d="M5.5,4.5 L6.8,4.3 L7.4,6.2 L6.6,6.9 Q7.4,8.7 9.1,9.4 L9.8,8.6 L11.7,9.2 L11.5,10.5 Q8.5,11.2 6.5,9.3 Q4.6,7.3 5.5,4.5 Z" fill="var(--white)"/></svg>(+33) 3.10.20.30.40</div>
    <div class="footer__web">www.parcelvue-example.fr &nbsp;|&nbsp; contact@parcelvue-example.fr</div>
  </footer>
</section>

</body>
</html>
```